KRT Flyer to attract applicants 11x17

Lantern Stagehand Collective provides crew for local concerts, filming, theater, and corporate events.
The flyer will be posted on bulletin boards at colleges with theater programs.
Our primary venues are historic theaters in downtown LA
Need a 11x17 poster to attract potential applicants/crew
I have attached a poster that one of our staff made that has all if the relevant info - but i know the poster can look much better than that. I have also attached many images and our logo. It is not necessary to use all of the images, or any of them. The two images of the theater interiors are the venues we operate so they would be the first to include. I can send additional info or images upon request. Thank you

Industry/Entity Type

Entertainment

Requirements
Must have
• APPLY@KRTCREW.EXAMPLE

```html
<!DOCTYPE html>
<html lang="en">
<head>
<meta charset="utf-8">
<title>Lantern Stagehand Collective – Open Positions</title>
<link href="https://fonts.googleapis.com/css2?family=Oswald:wght@200;600&family=Poppins:wght@600;700;800&display=swap" rel="stylesheet">
<style>
  :root {
    --navy: #0a2a6e;
    --navy-deep: #061a4a;
    --sky-light: #e6f1fb;
    --sky-mid: #c9def3;
    --yellow: #ffd600;
    --brand-blue: #0b55b5;
    --ink: #111111;
    --grey-text: #3a3a3a;
    --white: #ffffff;
  }
  * { margin: 0; padding: 0; box-sizing: border-box; }
  html, body { width: 864px; height: 1200px; overflow: hidden; background: var(--navy-deep); }
  .poster {
    position: relative; width: 864px; height: 1200px; overflow: hidden;
    font-family: "Poppins", sans-serif; color: var(--white);
  }
  .skyline-bg {
    position: absolute; inset: 0 0 auto 0; height: 780px;
    background: linear-gradient(180deg, #0a2a78 0%, #0b2c6f 40%, #0d2f63 70%, #0a2450 100%);
  }
  .swoosh { position: absolute; left: 0; top: 0; width: 864px; height: 1200px; }
  .crowd-bg {
    position: absolute; left: 0; right: 0; bottom: 0; height: 200px;
    background: linear-gradient(180deg, rgba(201,222,243,0) 0%, rgba(170,185,205,0.45) 100%);
  }
  .brand {
    position: absolute; top: 74px; left: 0; width: 864px;
    display: flex; justify-content: center; align-items: center; gap: 14px;
  }
  .brand-dot { width: 40px; height: 40px; border-radius: 50%; background: var(--white); }
  .brand-name { font-weight: 700; font-size: 22px; letter-spacing: 1px; color: var(--white); }
  .headline { font-size: inherit; font-weight: inherit; }
  .headline-has {
    position: absolute; top: 160px; left: 0; width: 864px; text-align: center;
    font-weight: 800; font-size: 76px; line-height: 1; letter-spacing: 1px;
  }
  .headline-open {
    position: absolute; top: 224px; left: 143px; width: 580px; text-align: center;
    font-weight: 800; font-size: 192px; line-height: 1; letter-spacing: -5px;
  }
  .headline-positions {
    position: absolute; top: 392px; left: 322px;
    display: inline-block; white-space: nowrap;
    font-family: "Oswald", sans-serif; font-weight: 600; font-size: 68px; line-height: 1;
    color: var(--yellow); letter-spacing: -1px;
    transform: scaleX(0.78); transform-origin: left top;
  }
  .photo { position: absolute; border: 2px solid var(--white); }
  .photo-theater-dome { left: 322px; top: 475px; width: 222px; height: 136px; background: linear-gradient(160deg, #5a2a6e 0%, #8a3b24 50%, #3a1a3a 100%); }
  .photo-theater-stage { left: 560px; top: 417px; width: 220px; height: 194px; background: linear-gradient(120deg, #c27a2a 0%, #8a4a1c 55%, #b0141a 80%, #1a0a0a 100%); }
  .photo-singer { left: 283px; top: 627px; width: 214px; height: 216px; background: radial-gradient(circle at 50% 35%, #e8eeff 0%, #5a6fd0 30%, #0c1033 75%); }
  .photo-console { left: 514px; top: 627px; width: 215px; height: 265px; background: linear-gradient(150deg, #2a2f3a 0%, #6a7a8a 45%, #2b3a55 100%); }
  .megaphone-art {
    position: absolute; left: 58px; top: 453px; width: 240px; height: 176px;
    background: linear-gradient(110deg, #3a1a6a 0%, #e04a2a 45%, #ffb020 75%, #8ad020 100%);
    border-radius: 40% 10% 20% 40%;
  }
  .lead-in {
    position: absolute; top: 850px; left: 108px;
    font-family: "Oswald", sans-serif; font-weight: 200; font-size: 48px; line-height: 1;
    color: var(--grey-text); letter-spacing: 1px; white-space: nowrap;
  }
  .role-title {
    position: absolute; top: 908px; left: 107px; white-space: nowrap;
    font-family: "Oswald", sans-serif; font-weight: 600; font-size: 71px; line-height: 1;
    color: var(--brand-blue); letter-spacing: -0.8px;
  }
  .role-sub {
    position: absolute; top: 994px; left: 110px; white-space: nowrap;
    font-weight: 600; font-size: 24px; line-height: 1; color: var(--ink); letter-spacing: 2px;
  }
  .apply-pill {
    position: absolute; top: 1040px; left: 106px; width: 652px; height: 40px;
    display: flex; border-radius: 10px; overflow: hidden; border: 1px solid var(--brand-blue);
  }
  .apply-label {
    width: 332px; background: var(--yellow); color: var(--ink);
    font-weight: 700; font-size: 19px; letter-spacing: 5px;
    display: flex; align-items: center; justify-content: center;
  }
  .apply-email {
    flex: 1; background: var(--brand-blue); color: var(--white);
    font-weight: 700; font-size: 17px; letter-spacing: 1px;
    display: flex; align-items: center; justify-content: center;
  }
  .website {
    position: absolute; top: 1122px; left: 0; width: 864px; text-align: center;
    font-weight: 700; font-size: 24px; letter-spacing: 4px; color: var(--ink);
  }
</style>
</head>
<body>
<main class="poster">
  <div class="skyline-bg" role="img" aria-label="Night city skyline in deep blue"></div>

  <svg class="swoosh" viewBox="0 0 864 1200" aria-hidden="true">
    <path d="M0,560 Q300,800 864,690 L864,1200 L0,1200 Z" fill="var(--yellow)"/>
    <path d="M0,660 Q330,830 864,726 L864,1200 L0,1200 Z" fill="var(--sky-light)"/>
  </svg>
  <div class="crowd-bg" role="img" aria-label="Faint concert crowd silhouettes"></div>

  <header class="brand">
    <span class="brand-dot"></span>
    <span class="brand-name">LANTERN STAGEHAND COLLECTIVE</span>
  </header>

  <h1 class="headline">
    <span class="headline-has">HAS</span>
    <span class="headline-open">OPEN</span>
    <span class="headline-positions">POSITIONS</span>
  </h1>

  <div class="megaphone-art" role="img" aria-label="Colourful megaphone illustration"></div>

  <div class="photo photo-theater-dome" role="img" aria-label="Ornate historic theater auditorium with domed ceiling"></div>
  <div class="photo photo-theater-stage" role="img" aria-label="Gilded historic theater interior with red stage curtain"></div>
  <div class="photo photo-singer" role="img" aria-label="Singer on stage in silhouette under spotlights"></div>
  <div class="photo photo-console" role="img" aria-label="Digital audio mixing console close-up"></div>

  <p class="lead-in">WE ARE LOOKING FOR</p>
  <h2 class="role-title">TALENTED TECHNICIANS</h2>
  <p class="role-sub">To add to our roster of skilled professionals</p>

  <div class="apply-pill">
    <span class="apply-label">SEND RESUME TO</span>
    <span class="apply-email">APPLY@KRTCREW.EXAMPLE</span>
  </div>

  <p class="website">www.krtcrew.example</p>
</main>
</body>
</html>
```